Indy Film Production Company/Studio

We need a business card designed from an existing logo. We are a digital studio/production company that caters to creating genre entertainment, like Action, Horror, and martial arts. The card along with the logo will be used to Brand the company from letter heads to banners. The design will also be used for postcards and Brochures. It should be professional and masculine.
Updates

Thank you to all the designers who have participated. I'm narrowing down who it will be. Thank you again.

Target Market(s)

Investors, Networks, Producers, and actors

Industry/Entity Type

Film Production

Contact Information for Business Card

Benedikt Harwell
Producer/Writer/Director
www.copperlatchpictures.com

Requirements
Must have
• Website address, Facebook icon and Twitter icon possibly in the back of the card.
Nice to have
• Logline of Company: Follow The Action.

```html
<!DOCTYPE html>
<html lang="en">
<head>
<meta charset="utf-8">
<title>Copper Latch Pictures – Business Card</title>
<link rel="stylesheet" href="https://fonts.googleapis.com/css2?family=Montserrat:ital,wght@1,800&family=Roboto:wght@400;700;900&display=swap">
<style>
  :root {
    --bg: #c9c7c8;
    --brand-red: #cf3029;
    --paper: #f4f4f2;
    --ink: #1c1c1c;
    --ink-soft: #333333;
    --charcoal: #2a2828;
  }
  * { box-sizing: border-box; margin: 0; padding: 0; }
  html, body {
    width: 1200px; height: 1200px; overflow: hidden;
    background: var(--bg);
    font-family: "Roboto", Arial, sans-serif;
  }
  .card {
    position: absolute;
    left: 248px;
    width: 704px;
    height: 418px;
    overflow: hidden;
  }
  .card--front { top: 118px; background: var(--brand-red); }
  .card--back  { top: 645px; background: var(--paper); }

  .front-wordmark {
    position: absolute; left: 0; right: 0; top: 182px;
    text-align: center;
    color: var(--paper);
    font-weight: 900; font-size: 38px; letter-spacing: 1px;
    text-transform: uppercase;
  }

  .back-wordmark {
    position: absolute; left: 38px; top: 78px;
    color: var(--brand-red);
    font-weight: 900; font-size: 32px; letter-spacing: 1px;
    line-height: 1.1;
    text-transform: uppercase;
  }

  .rule {
    position: absolute; left: 38px; top: 253px;
    width: 482px; height: 2px; background: var(--brand-red);
  }

  .contact-list {
    position: absolute; left: 38px; top: 281px;
    list-style: none;
  }
  .contact-list li {
    display: flex; align-items: center;
    height: 27.5px;
    font-size: 18px; color: var(--ink-soft);
  }
  .contact-list svg { width: 16px; height: 16px; margin-right: 19px; fill: var(--brand-red); }

  .person {
    position: absolute; right: 42px; top: 195px; text-align: right;
  }
  .person__name {
    font-family: "Montserrat", "Arial Black", sans-serif;
    font-style: italic; font-weight: 800;
    font-size: 25px; color: var(--ink);
  }
  .person__role { margin-top: 10px; font-size: 16px; color: var(--ink-soft); }

  .address {
    position: absolute; right: 42px; top: 292px;
    text-align: right; font-size: 18px; line-height: 29px; color: var(--ink-soft);
  }

  .footer-bands { position: absolute; left: 0; bottom: 0; width: 704px; height: 40px; }
</style>
</head>
<body>

<section class="card card--front">
  <div class="front-wordmark">Copper Latch Pictures</div>
</section>

<section class="card card--back">
  <div class="back-wordmark">Copper Latch<br>Pictures</div>

  <div class="person">
    <div class="person__name">Benedikt Harwell</div>
    <div class="person__role">Managing Director</div>
  </div>

  <div class="rule"></div>

  <ul class="contact-list">
    <li>
      <svg viewBox="0 0 16 16" aria-hidden="true"><path d="M3 5c0-2 2-3 5-3s5 1 5 3v1h-3V5H6v1H3z M4 8l2-2h4l2 2v6H4z"/><circle cx="8" cy="10.5" r="1.6" fill="var(--paper)"/></svg>
      5550142817
    </li>
    <li>
      <svg viewBox="0 0 16 16" aria-hidden="true"><circle cx="8" cy="8" r="7"/><path d="M1 8h14M8 1c-3 3-3 11 0 14M8 1c3 3 3 11 0 14" stroke="var(--paper)" stroke-width="1.2" fill="none"/></svg>
      www.copperlatchpictures.com
    </li>
    <li>
      <svg viewBox="0 0 16 16" aria-hidden="true"><rect x="1" y="3" width="14" height="10"/><path d="M1.5 3.5 8 9l6.5-5.5" stroke="var(--paper)" stroke-width="1.3" fill="none"/></svg>
      hello@copperlatchpictures.com
    </li>
  </ul>

  <div class="address">Your Long Commercial or<br>business address in 2 line</div>

  <svg class="footer-bands" viewBox="0 0 704 40" aria-hidden="true">
    <polygon points="0,18 392,18 382,40 0,40" fill="var(--charcoal)"/>
    <polygon points="398,0 704,0 704,40 376,40" fill="var(--brand-red)"/>
  </svg>
</section>

</body>
</html>
```